Business Card Design using new attached logo

We are a family run Plumbing and Heating firm looking to improve our company image with an improved business card and new logo.We are looking to keep the company colour (Blue) involved in our design

Reason: New logo added which needs to be incorporated on designs

Industry/Entity Type

Business

Contact Information for Business Card

See attachment of all info required.

Requirements
Must have
• We have just picked a new company logo which is attached.
• Could you please provide your business card designs using this logo.
• We are looking for the logo on the back as well as the front with all the info required

```html
<!DOCTYPE html>
<html lang="en">
<head>
<meta charset="utf-8">
<title>Halden Services Ltd – Business Card</title>
<link href="https://fonts.googleapis.com/css2?family=Lato:wght@400;700&display=swap" rel="stylesheet">
<style>
  :root {
    --brand-blue: #0d2dff;
    --ink: #111111;
    --panel-black: #0d0d0d;
    --paper: #ffffff;
  }
  * { box-sizing: border-box; margin: 0; padding: 0; }
  html, body { width: 720px; height: 1200px; overflow: hidden; background: var(--paper); }
  .card {
    position: relative;
    width: 720px;
    height: 1200px;
    background: var(--paper);
    font-family: "Lato", Arial, sans-serif;
    overflow: hidden;
  }
  .top-rule {
    position: absolute; left: 81px; top: 79px;
    width: 559px; height: 5px; background: var(--brand-blue);
  }
  .brand {
    position: absolute; left: 0; top: 250px; width: 720px;
    text-align: center; color: var(--ink); font-weight: 400;
  }
  .brand-mark {
    width: 60px; height: 60px; margin: 0 auto 14px;
    background: var(--brand-blue);
  }
  .brand-name { font-size: 49px; line-height: 1; letter-spacing: 0.5px; }
  .brand-suffix { font-size: 34px; line-height: 1; margin-top: 10px; }

  .name-band {
    position: absolute; left: 0; top: 594px; width: 720px; height: 132px;
    background: var(--brand-blue); color: var(--paper);
  }
  .name-band .icon { position: absolute; left: 83px; top: 44px; }
  .person-name {
    position: absolute; left: 170px; top: 26px;
    font-size: 45px; font-weight: 400; line-height: 1;
  }
  .person-name strong { font-weight: 700; }
  .person-role {
    position: absolute; left: 170px; top: 73px;
    font-size: 24px; line-height: 1;
  }

  .contact-panel {
    position: absolute; left: 0; top: 726px; width: 720px; height: 393px;
    background: var(--panel-black); color: var(--paper);
  }
  .divider {
    position: absolute; left: 0; width: 720px; height: 4px; background: var(--brand-blue);
  }
  .divider.first { top: 128px; }
  .divider.second { top: 261px; }

  .row { position: absolute; left: 0; width: 720px; }
  .row .icon { position: absolute; left: 84px; }
  .row .text { position: absolute; left: 169px; font-size: 26px; line-height: 1; letter-spacing: 0.3px; }

  .row.phone { top: 14px; }
  .row.fax { top: 57px; }
  .row.mobile { top: 94px; }
  .row.phone .icon, .row.fax .icon, .row.mobile .icon { top: 0; }
  .row.phone .text, .row.fax .text, .row.mobile .text { top: 1px; }

  .row.email { top: 176px; }
  .row.email .icon { left: 83px; top: 0; }
  .row.email .text { left: 170px; top: 7px; font-size: 30px; }

  .row.address { top: 306px; }
  .row.address .icon { left: 90px; top: 0; }
  .row.address .text { left: 170px; top: -8px; font-size: 30px; line-height: 37px; }

  .foot-band {
    position: absolute; left: 0; top: 1119px; width: 720px; height: 81px;
    background: var(--brand-blue);
  }
</style>
</head>
<body>
<main class="card">
  <div class="top-rule"></div>

  <header class="brand">
    <div class="brand-mark"></div>
    <div class="brand-name">HALDEN SERVICES</div>
    <div class="brand-suffix">LTD</div>
  </header>

  <section class="name-band">
    <svg class="icon" width="42" height="42" viewBox="0 0 42 42" aria-hidden="true">
      <circle cx="21" cy="12" r="10" fill="#fff"/>
      <path d="M1 42 C1 30 10 25 21 25 C32 25 41 30 41 42 Z" fill="#fff"/>
    </svg>
    <div class="person-name"><strong>MARK</strong> FENWICK</div>
    <div class="person-role">Director</div>
  </section>

  <section class="contact-panel">
    <div class="row phone">
      <svg class="icon" width="28" height="26" viewBox="0 0 28 26" aria-hidden="true">
        <path d="M2 9 C2 3 26 3 26 9 L22 10 L20 6 L8 6 L6 10 Z" fill="#fff"/>
        <path d="M8 10 L20 10 L26 22 L26 25 L2 25 L2 22 Z" fill="#fff"/>
        <circle cx="14" cy="17" r="3.5" fill="#0d0d0d"/>
      </svg>
      <span class="text">+020&nbsp;&nbsp;8123&nbsp;&nbsp;4567</span>
    </div>
    <div class="row fax">
      <svg class="icon" width="28" height="26" viewBox="0 0 28 26" aria-hidden="true">
        <rect x="7" y="1" width="14" height="7" fill="#fff"/>
        <rect x="1" y="9" width="26" height="11" rx="2" fill="#fff"/>
        <rect x="7" y="15" width="14" height="10" fill="#fff" stroke="#0d0d0d" stroke-width="2"/>
      </svg>
      <span class="text">+020&nbsp;&nbsp;8123&nbsp;&nbsp;4590</span>
    </div>
    <div class="row mobile">
      <svg class="icon" width="28" height="28" viewBox="0 0 28 28" aria-hidden="true">
        <rect x="7" y="1" width="14" height="26" rx="2" fill="none" stroke="#fff" stroke-width="2"/>
        <line x1="7" y1="5" x2="21" y2="5" stroke="#fff" stroke-width="1.5"/>
        <line x1="7" y1="22" x2="21" y2="22" stroke="#fff" stroke-width="1.5"/>
      </svg>
      <span class="text">+07700 900123</span>
    </div>

    <div class="divider first"></div>

    <div class="row email">
      <svg class="icon" width="42" height="42" viewBox="0 0 42 42" aria-hidden="true">
        <g fill="none" stroke="#fff" stroke-width="3">
          <circle cx="21" cy="21" r="19"/>
          <ellipse cx="21" cy="21" rx="8" ry="19"/>
          <line x1="21" y1="2" x2="21" y2="40"/>
          <line x1="2" y1="21" x2="40" y2="21"/>
          <path d="M5 11 H37 M5 31 H37"/>
        </g>
      </svg>
      <span class="text">markfenwick@haldenservices.co.uk</span>
    </div>

    <div class="divider second"></div>

    <div class="row address">
      <svg class="icon" width="28" height="42" viewBox="0 0 28 42" aria-hidden="true">
        <path d="M14 1 C6 1 1 7 1 14 C1 24 14 41 14 41 C14 41 27 24 27 14 C27 7 22 1 14 1 Z" fill="#fff"/>
        <circle cx="14" cy="14" r="5" fill="#0d0d0d"/>
      </svg>
      <span class="text">14 Mill Parade, Alder Road,<br>Redford, Surrey RD2 5QT</span>
    </div>
  </section>

  <div class="foot-band"></div>
</main>
</body>
</html>
```